"Savour the Heritage" Packaging Design

We are a manufacturer and distributor of various ethnic and traditional snacks like cassava chips, murukku, shrimp chips, and mostly potato-based pellets.

The new packaging design should evoke a whole new respect for traditional ethnic snacks. We would like to pursue "ONE" common packaging for all products due to our wide product range and economical reasons. This will mostly be feasible through a 'See-Through" window on the packaging.

We would like to see our packaging literally shines under reflection during display using our high gloss plastic material (OPP/PET/MPET/CPP). The base color should contrast well with the logo, the slogan and as well as other information that we would like to showcase.

Gradually, we want to set out to be the clear choice for traditional snacks go-to. Though generic and simple, we hope to communicate values of elegant packaging visuals, clear content showcase and easy brand identification.

I have uploaded a 'rough' idea in the attachment and we hope to see a vast improved versions of it or whole new concepts that's compatible, as long as they all kick ass.
Updates

Hi Designers,

I have uploaded a new attachment "Idea 2" for your kind review and consideration.

Please do give it a try. I hope you guys do.

Regards
Marcus

Hi Designers,

Packaging Idea 3 has been attached as well.

Please do try all!

Regards
Marcus

Target Market(s)

Mid 20s blue-collared working adults to housemakers in their 50s.

Industry/Entity Type

Pet

Requirements
Must have
• 1. Kelim Lodge Brand Logo (Front)
2. "Savour the Heritage" Slogan (Front)
3. Established Since 1980s. (Front)
4. "Halal Logo" (Front)
5. The 'See Through' window must be consists at least 40% of the front panel.
6. The whole packaging must produce a glossy, shiny effect.
7. To include a Generic "back panel" of a typical snack packaging which afterwards I will update on myself. (Nutritional Information, Description, Company's Info, Product of Origin, barcodes, Batch Number, Best Before Date and etc).
Nice to have
• 1. The "shiny feel" of the packaging should somehow match or surpass an effect I stumble upon in a website,
http://www.fernquay.com.my/

2. The base color we have in mind can be found in the attachment. (Patone 021C, Lamination on MPET to produce a shiny glossy effect) So please do simulate the effect on the design anyway.

Give it all you got!
Should not have
• No Zip Locks on the packaging.

```html
<!DOCTYPE html>
<html lang="en">
<head>
<meta charset="utf-8">
<title>Kelim Lodge – Snack Pouch Front</title>
<link href="https://fonts.googleapis.com/css2?family=Dancing+Script:wght@600;700&family=Open+Sans:wght@700;800&family=Libre+Baskerville&display=swap" rel="stylesheet">
<style>
  :root {
    --maroon: #8a1519;
    --red: #d6261d;
    --orange: #f08a1c;
    --gold: #f7b52a;
    --yellow: #fde03a;
    --ribbon-dark: #e08a12;
    --ribbon-light: #fbd37a;
    --white: #ffffff;
    --ink: #2a1a10;
    --badge-grey: #9fb8a8;
  }
  * { margin: 0; padding: 0; box-sizing: border-box; }
  html, body { width: 834px; height: 1200px; overflow: hidden; background: #fff; }
  .pouch {
    position: relative;
    width: 834px;
    height: 1200px;
    overflow: hidden;
    font-family: "Open Sans", sans-serif;
  }
  .pouch__field {
    position: absolute;
    inset: 0;
    background:
      radial-gradient(ellipse 260px 420px at 0% 62%, var(--yellow) 0%, rgba(253,224,58,0) 100%),
      radial-gradient(ellipse 330px 520px at 100% 38%, var(--yellow) 0%, rgba(253,224,58,0.6) 35%, rgba(253,224,58,0) 100%),
      linear-gradient(135deg, var(--red) 0%, #e2421c 35%, var(--orange) 60%, var(--red) 100%);
  }
  .pouch__seal {
    position: absolute;
    left: 0; right: 0;
    background: var(--maroon);
  }
  .pouch__seal--top { top: 0; height: 98px; }
  .pouch__seal--bottom { bottom: 0; height: 70px; }
  .hang-hole {
    position: absolute;
    left: 401px; top: 26px;
    width: 36px; height: 36px;
    border-radius: 50%;
    background: var(--white);
    box-shadow: inset 2px 3px 4px rgba(0,0,0,0.35);
  }
  .window {
    position: absolute;
    left: 118px; top: 416px;
    width: 616px; height: 636px;
    background: var(--white);
    border-radius: 72px 72px 104px 104px;
  }
  .ribbon { position: absolute; left: 0; top: 0; }
  .brand-name {
    position: absolute;
    left: 0; right: 0; top: 196px;
    text-align: center;
    font-family: "Open Sans", sans-serif;
    font-weight: 800;
    font-size: 62px;
    line-height: 80px;
    color: var(--white);
  }
  .slogan {
    position: absolute;
    left: 0; right: 0; top: 382px;
    text-align: center;
    font-family: "Dancing Script", cursive;
    font-weight: 700;
    font-size: 42px;
    color: var(--white);
  }
  .established {
    position: absolute;
    left: 0; right: 0; top: 450px;
    text-align: center;
    font-family: "Libre Baskerville", serif;
    font-size: 16px;
    color: var(--ink);
  }
  .name-band {
    position: absolute;
    left: 118px; top: 856px;
    width: 616px; height: 108px;
    background: linear-gradient(90deg, var(--ribbon-dark) 0%, var(--gold) 30%, var(--gold) 70%, var(--ribbon-dark) 100%);
    border-top: 3px solid var(--ribbon-light);
    border-bottom: 3px solid #b8860f;
    display: flex;
    align-items: center;
    justify-content: center;
  }
  .name-band__label {
    font-family: "Dancing Script", cursive;
    font-weight: 600;
    font-size: 52px;
    color: var(--white);
    text-shadow: 1px 2px 2px rgba(0,0,0,0.35);
  }
  .cert { position: absolute; border-radius: 50%; }
  .cert--hygiene { left: 534px; top: 995px; width: 42px; height: 42px; border: 3px solid #1a120c; background: var(--white); }
  .cert--halal { left: 588px; top: 990px; width: 52px; height: 52px; background: var(--badge-grey); border: 2px solid #6f8a7a; }
  .net-weight {
    position: absolute;
    left: 0; right: 0; top: 1074px;
    text-align: center;
    font-weight: 700;
    font-size: 29px;
    color: var(--white);
    text-shadow: 1px 2px 3px rgba(0,0,0,0.4);
  }
</style>
</head>
<body>
<div class="pouch">
  <div class="pouch__field" role="img" aria-label="Glossy red to golden gradient background with a faint damask pattern"></div>
  <div class="pouch__seal pouch__seal--top"></div>
  <div class="pouch__seal pouch__seal--bottom"></div>
  <div class="hang-hole"></div>

  <div class="window"></div>

  <svg class="ribbon" width="834" height="500" viewBox="0 0 834 500" aria-hidden="true">
    <defs>
      <linearGradient id="ribbonFace" x1="0" y1="0" x2="1" y2="0">
        <stop offset="0" stop-color="#e58a10"/>
        <stop offset="0.5" stop-color="#f9a81e"/>
        <stop offset="1" stop-color="#e58a10"/>
      </linearGradient>
      <linearGradient id="ribbonFold" x1="0" y1="0" x2="0" y2="1">
        <stop offset="0" stop-color="#fde6a8"/>
        <stop offset="1" stop-color="#e7a232"/>
      </linearGradient>
    </defs>
    <path d="M72 346 L108 258 Q200 262 290 300 L286 368 Q180 330 72 346 Z" fill="url(#ribbonFace)"/>
    <path d="M762 346 L726 258 Q634 262 544 300 L548 368 Q654 330 762 346 Z" fill="url(#ribbonFace)"/>
    <path d="M168 316 Q220 300 286 330 L282 372 Q230 350 180 360 Z" fill="url(#ribbonFold)"/>
    <path d="M666 316 Q614 300 548 330 L552 372 Q604 350 654 360 Z" fill="url(#ribbonFold)"/>
    <path d="M140 360 Q417 280 700 360 L690 430 Q417 520 150 430 Z" fill="url(#ribbonFace)"/>
    <path d="M150 430 Q417 520 690 430" fill="none" stroke="#fbd37a" stroke-width="3"/>
  </svg>

  <p class="brand-name">Kelim Lodge</p>

  <p class="slogan">Savour the Heritage</p>
  <p class="established">Established Since 1980</p>

  <div class="name-band">
    <span class="name-band__label">snack name goes here</span>
  </div>

  <div class="cert cert--hygiene"></div>
  <div class="cert cert--halal"></div>

  <p class="net-weight">Net Wt. : 200gms</p>
</div>
</body>
</html>
```